Door Hanger / Brochure / Work Estimate Sheet
Brightwell Scrubbing & Remodel Services
pelund - if the design was not submitted it cannot be considered for final judgement.
A winner has been selected. They will be notified shortly.
wendal, had this marvelous design, but just when i was about to upload, my network went down. what happens now?
Contest is extended for 2 more days.
-Pam
The designs are looking great so far. Just to clarify:
1. I would like to see a 3 fold brochure.
2. I would like to have something that looks like "stik-em" notes pasted on the brochure. I will be uploading an example of what I'm talking about. I DO NOT want to copy the template that I'm uploading I just want to see the "stik-em" notes on the brochure.
3. On the back panel, I would like to see a check-list that a customer could check off some of the items that they would like done in their home.

```html
<!DOCTYPE html>
<html lang="en">
<head>
<meta charset="utf-8">
<title>Brightwell Scrubbing &amp; Remodel Services – Print Set</title>
<link href="https://fonts.googleapis.com/css2?family=Cinzel:wght@600&family=Arimo:wght@400;700&display=swap" rel="stylesheet">
<style>
:root{
  --green:#6aa52a;
  --green-light:#a6cf3a;
  --green-pale:#e6f1cf;
  --blue:#1d4f91;
  --ink:#333;
  --grey:#8a8a8a;
  --paper:#fff;
  --bg:#fff;
  --note:#fff27a;
  --line:#c9c9c9;
}
*{box-sizing:border-box;margin:0;padding:0}
html,body{width:1200px;height:826px;overflow:hidden;background:var(--bg)}
body{position:relative;font-family:"Arimo",Arial,sans-serif;color:var(--ink)}
.piece{position:absolute;background:var(--paper);box-shadow:0 2px 6px rgba(0,0,0,.25);overflow:hidden}
.brand{font-family:"Cinzel",serif;font-weight:600;color:var(--blue);line-height:1.1}
.photo{position:absolute}
.photo-worker{background:linear-gradient(160deg,#c8c6c2,#6d6a66 55%,#3d3b39)}
.photo-spill{background:radial-gradient(circle at 45% 55%,#6b4a2f,#a98b6c 55%,#e2d6c7)}
.photo-room{background:linear-gradient(150deg,#d9d2c5,#a89c8a)}
.photo-tools{background:linear-gradient(160deg,#e5c36a,#9d6b32)}
.photo-dog{background:linear-gradient(160deg,#e9e6e1,#7d7873)}
.leaves{position:absolute;background:radial-gradient(ellipse at 60% 40%,var(--green-light),var(--green) 70%,rgba(106,165,42,0) 72%)}
.panel{position:absolute;top:0;bottom:0}
.heading{color:var(--green);font-weight:700}
.list{list-style:none;font-size:7px;line-height:11px}
.list li::before{content:"";display:inline-block;width:5px;height:5px;border:1px solid var(--green);margin-right:4px}
.tagline{color:var(--green);font-family:"Cinzel",serif;font-weight:600;text-align:center}
.contact{font-size:8px;line-height:12px;color:var(--ink)}
.note{position:absolute;background:var(--note);width:44px;height:40px;padding:4px;font-size:5.5px;line-height:7px;box-shadow:1px 2px 3px rgba(0,0,0,.25)}
.note::before{content:"";position:absolute;top:-3px;left:18px;width:7px;height:7px;border-radius:50%;background:#d33}
.vertical{position:absolute;writing-mode:vertical-rl;transform:rotate(180deg);color:var(--green);font-weight:700}
.sheet-row{height:14px;border-bottom:1px solid var(--line)}
</style>
</head>
<body>

<!-- Brochure outside -->
<section class="piece brochure-outside" style="left:24px;top:26px;width:540px;height:500px">
  <div class="panel" style="left:0;width:180px;padding:22px 14px">
    <h3 class="heading" style="font-size:14px;margin-bottom:10px">Way to Go</h3>
    <p class="heading" style="font-size:9px;margin-bottom:4px">Cleaning Services</p>
    <ul class="list" style="margin-bottom:12px">
      <li>Carpet cleaning</li><li>Upholstery cleaning</li><li>Tile &amp; grout cleaning</li>
      <li>Window washing</li><li>Move-in &amp; move-out cleaning</li><li>Office cleaning</li>
      <li>Floor waxing</li><li>Pressure washing</li>
    </ul>
    <p class="heading" style="font-size:9px;margin-bottom:4px">Home Improvement &amp; Emergency Services</p>
    <ul class="list">
      <li>Water damage restoration</li><li>Mold removal</li><li>Painting</li>
      <li>Drywall repair</li><li>Flooring installs</li><li>Kitchen updates</li>
      <li>Bathroom remodels</li><li>Fire damage clean-up</li><li>Storm board-up</li><li>Odor removal</li>
    </ul>
    <div class="photo photo-spill" role="img" aria-label="Spilled coffee cup on a carpet" style="left:0;bottom:0;width:120px;height:110px;border-top-right-radius:60px"></div>
  </div>
  <div class="panel" style="left:180px;width:180px">
    <svg width="180" height="500" style="position:absolute;left:0;top:0" aria-hidden="true">
      <path d="M0 440 C60 400 130 420 180 380 L180 500 L0 500Z" fill="var(--green-pale)"/>
      <path d="M0 452 C70 410 130 430 180 392" stroke="var(--green)" stroke-width="3" fill="none"/>
    </svg>
    <div class="leaves" role="img" aria-label="Green leaf spray" style="left:60px;top:10px;width:120px;height:120px"></div>
    <p class="brand" style="position:absolute;left:14px;top:200px;width:152px;font-size:12px">Brightwell Scrubbing &amp; Remodel Services</p>
    <div class="contact" style="position:absolute;left:40px;top:262px">
      <p>☎ (555) 014-2290</p><p>☎ (555) 014-2291</p><p>hello@brightwellsrs.com</p><p>www.brightwellsrs.com</p>
    </div>
  </div>
  <div class="panel" style="left:360px;width:180px">
    <div class="photo photo-worker" role="img" aria-label="Technician cleaning a carpet with an extractor wand" style="left:14px;top:16px;width:150px;height:230px;border-radius:0 0 80px 0"></div>
    <div class="leaves" role="img" aria-label="Green leaf spray" style="left:110px;top:0;width:80px;height:120px"></div>
    <svg width="180" height="500" style="position:absolute;left:0;top:0" aria-hidden="true">
      <path d="M0 270 C60 250 120 240 180 200" stroke="var(--green)" stroke-width="4" fill="none"/>
      <path d="M0 282 C70 262 120 256 180 220" stroke="var(--green-light)" stroke-width="2" fill="none"/>
      <circle cx="24" cy="320" r="9" fill="var(--green)"/>
    </svg>
    <p class="brand" style="position:absolute;left:40px;top:308px;width:130px;font-size:13px">Brightwell Scrubbing &amp; Remodel Services</p>
    <p class="contact" style="position:absolute;left:40px;top:372px">☎ (555) 014-2290</p>
    <p class="tagline" style="position:absolute;left:10px;right:10px;bottom:34px;font-size:11px">Don't forget to ask about our specials</p>
  </div>
</section>

<!-- Brochure inside -->
<section class="piece brochure-inside" style="left:24px;top:552px;width:540px;height:252px;background:#f3f3f1">
  <p class="vertical" style="left:6px;top:20px;font-size:10px">Cleaning Services</p>
  <div class="note" style="left:28px;top:18px;transform:rotate(-3deg)">Deep carpet cleaning for every room</div>
  <div class="note" style="left:84px;top:14px;transform:rotate(2deg)">Tile &amp; grout made new again</div>
  <div class="note" style="left:140px;top:20px;transform:rotate(-2deg)">Upholstery fresh and spotless</div>
  <div class="note" style="left:40px;top:72px;transform:rotate(3deg)">Windows washed inside &amp; out</div>
  <div class="note" style="left:100px;top:74px;transform:rotate(-4deg)">Move-out clean, keep deposit</div>
  <div class="note" style="left:158px;top:78px;transform:rotate(2deg)">Offices kept tidy each week</div>
  <div class="note" style="left:60px;top:128px;transform:rotate(-2deg)">Pressure wash decks &amp; drives</div>
  <div class="photo photo-dog" role="img" aria-label="Dog sitting on a clean carpet" style="left:20px;top:180px;width:110px;height:72px"></div>
  <div class="photo photo-tools" role="img" aria-label="Tool belt worn by a contractor" style="left:200px;top:118px;width:100px;height:110px;border-radius:50%"></div>
  <div class="photo photo-room" role="img" aria-label="Remodeled kitchen interior" style="left:330px;top:14px;width:110px;height:110px;border-radius:50%"></div>
  <div class="photo photo-room" role="img" aria-label="Renovated living room" style="left:420px;top:70px;width:100px;height:100px;border-radius:50%"></div>
  <div class="leaves" role="img" aria-label="Green leaf spray" style="left:270px;top:0;width:80px;height:60px"></div>
  <div class="note" style="left:360px;top:140px;transform:rotate(3deg)">Painting and drywall repair</div>
  <div class="note" style="left:440px;top:176px;transform:rotate(-3deg)">Fast help after water damage</div>
  <p class="tagline" style="position:absolute;left:260px;bottom:8px;font-size:10px">Home Improvement &amp; Emergency Services</p>
</section>

<!-- Rack cards -->
<section class="piece rack-card" style="left:588px;top:30px;width:120px;height:484px">
  <div class="leaves" role="img" aria-label="Green leaf spray" style="left:30px;top:0;width:90px;height:90px"></div>
  <div class="photo photo-worker" role="img" aria-label="Technician cleaning a carpet with an extractor wand" style="left:8px;top:50px;width:104px;height:200px;border-radius:0 0 60px 0"></div>
  <svg width="120" height="484" style="position:absolute;left:0;top:0" aria-hidden="true">
    <path d="M0 280 C40 266 80 262 120 236" stroke="var(--green)" stroke-width="3" fill="none"/>
  </svg>
  <p class="brand" style="position:absolute;left:10px;top:300px;width:100px;font-size:10px">Brightwell Scrubbing &amp; Remodel Services</p>
  <p class="tagline" style="position:absolute;left:6px;right:6px;bottom:40px;font-size:8px">Don't forget to ask about our specials</p>
</section>
<section class="piece rack-card" style="left:684px;top:26px;width:120px;height:488px">
  <div class="leaves" role="img" aria-label="Green leaf spray" style="left:30px;top:0;width:90px;height:90px"></div>
  <div class="photo photo-worker" role="img" aria-label="Technician cleaning a carpet with an extractor wand" style="left:8px;top:50px;width:104px;height:200px;border-radius:0 0 60px 0"></div>
  <svg width="120" height="488" style="position:absolute;left:0;top:0" aria-hidden="true">
    <path d="M0 280 C40 266 80 262 120 236" stroke="var(--green)" stroke-width="3" fill="none"/>
    <path d="M0 290 C40 278 80 274 120 250" stroke="var(--green-light)" stroke-width="2" fill="none"/>
  </svg>
  <p class="brand" style="position:absolute;left:10px;top:300px;width:100px;font-size:10px">Brightwell Scrubbing &amp; Remodel Services</p>
  <p class="contact" style="position:absolute;left:10px;top:350px;font-size:7px">☎ (555) 014-2290</p>
  <p class="tagline" style="position:absolute;left:6px;right:6px;bottom:40px;font-size:8px">Don't forget to ask about our specials</p>
</section>

<!-- Work estimate sheet -->
<section class="piece estimate-sheet" style="left:830px;top:30px;width:346px;height:462px;padding:16px">
  <p style="position:absolute;right:16px;top:10px;font-size:7px;color:var(--grey)">WORK ESTIMATE · No. ______</p>
  <div class="leaves" role="img" aria-label="Green leaf spray" style="left:14px;top:20px;width:40px;height:40px"></div>
  <p class="brand" style="position:absolute;left:58px;top:32px;width:140px;font-size:9px">Brightwell Scrubbing &amp; Remodel Services</p>
  <div class="contact" style="position:absolute;left:58px;top:62px;font-size:6px;line-height:8px;color:var(--blue)">
    <p>☎ (555) 014-2290 · (555) 014-2291</p><p>hello@brightwellsrs.com</p>
  </div>
  <div style="position:absolute;right:16px;top:32px;width:110px;font-size:6px;line-height:12px;color:var(--grey)">
    <p>Date: ____________</p><p>Phone: ___________</p><p>Rep: _____________</p>
  </div>
  <div style="position:absolute;left:16px;right:16px;top:100px;height:36px;border:1px solid var(--line);font-size:6px;padding:3px;color:var(--grey)">Customer name &amp; address</div>
  <div style="position:absolute;left:16px;right:16px;top:146px;height:186px;border:1px solid var(--line)">
    <div style="height:12px;background:var(--green-pale);font-size:6px;padding:2px 4px;color:var(--ink)">Description of work</div>
    <div class="sheet-row"></div><div class="sheet-row"></div><div class="sheet-row"></div><div class="sheet-row"></div>
    <div class="sheet-row"></div><div class="sheet-row"></div><div class="sheet-row"></div><div class="sheet-row"></div>
    <div class="sheet-row"></div><div class="sheet-row"></div><div class="sheet-row"></div>
  </div>
  <div style="position:absolute;right:16px;top:340px;width:110px;font-size:6px;line-height:12px;color:var(--grey)">
    <p style="border:1px solid var(--line);padding:0 3px">Subtotal</p>
    <p style="border:1px solid var(--line);padding:0 3px">Tax</p>
    <p style="border:1px solid var(--line);padding:0 3px">Total</p>
  </div>
  <div style="position:absolute;left:16px;right:16px;bottom:22px;height:40px;border:1px solid var(--line);font-size:6px;padding:3px;color:var(--grey)">This estimate is valid for thirty days. Signature: ____________</div>
</section>

<!-- Door hangers -->
<section class="piece door-hanger" style="left:598px;top:576px;width:104px;height:236px">
  <svg width="104" height="236" style="position:absolute;left:0;top:0" aria-hidden="true">
    <circle cx="52" cy="34" r="20" fill="var(--bg)" stroke="var(--line)"/>
    <path d="M52 14 L52 0" stroke="var(--line)"/>
  </svg>
  <div class="leaves" role="img" aria-label="Green leaf spray" style="left:0;top:0;width:40px;height:40px"></div>
  <p class="heading" style="position:absolute;left:8px;top:70px;font-size:7px">Cleaning Services</p>
  <ul class="list" style="position:absolute;left:8px;top:82px;font-size:5.5px;line-height:9px">
    <li>Carpet</li><li>Upholstery</li><li>Tile &amp; grout</li><li>Windows</li><li>Floors</li>
    <li>Painting</li><li>Drywall</li><li>Water damage</li><li>Mold removal</li><li>Remodels</li>
  </ul>
  <div style="position:absolute;left:0;right:0;bottom:0;height:18px;background:var(--green);color:#fff;font-size:6px;text-align:center;line-height:18px">Call us today!</div>
</section>
<section class="piece door-hanger" style="left:694px;top:560px;width:110px;height:256px">
  <svg width="110" height="256" style="position:absolute;left:0;top:0" aria-hidden="true">
    <circle cx="55" cy="34" r="20" fill="var(--bg)" stroke="var(--line)"/>
    <path d="M55 14 L55 0" stroke="var(--line)"/>
    <path d="M0 180 C40 168 80 166 110 146" stroke="var(--green)" stroke-width="3" fill="none"/>
  </svg>
  <div class="leaves" role="img" aria-label="Green leaf spray" style="left:70px;top:40px;width:40px;height:50px"></div>
  <div class="photo photo-worker" role="img" aria-label="Technician cleaning a carpet with an extractor wand" style="left:8px;top:62px;width:94px;height:110px;border-radius:0 0 50px 0"></div>
  <p class="brand" style="position:absolute;left:8px;top:190px;width:96px;font-size:8px">Brightwell Scrubbing &amp; Remodel Services</p>
  <div style="position:absolute;left:0;right:0;bottom:0;height:20px;background:var(--green);color:#fff;font-size:7px;text-align:center;line-height:20px">☎ (555) 014-2290</div>
</section>

<!-- Brand name -->
<section class="brand-lockup" style="position:absolute;left:900px;top:722px;width:276px;height:82px;display:flex;align-items:center;gap:12px">
  <span style="width:40px;height:40px;border-radius:50%;background:var(--green);flex:none"></span>
  <p class="brand" style="font-size:17px">Brightwell Scrubbing &amp; Remodel Services</p>
</section>

</body>
</html>
```